Carpal Tunnel - PPC Landing Page

We need to do a SINGLE page landing page for a doctor who specializes in Carpal Tunnel syndrome - please research if you're not familiar - it's very common.

Landing page essentials:
Must have a form in upper right hand corner:
Form title: "Get a free diagnosis."
Form inputs: Name, Phone, Email, Requested Appointment time

Page is for PPC, so needs to be simple and light on content. Content has been provided and attached to this project.

No navigation, just a single page.

Industry/Entity Type

Health

Coding

Coded - Design and coding required

Number of Pages Required

1 page

Requirements
Must have
• Elegant look - Conversion optimized for form and phone
• Responsive design.
Should not have
• Old outdated images.

```html
<!DOCTYPE html>
<html lang="en">
<head>
<meta charset="utf-8">
<title>Carpal Tunnel Syndrome</title>
<link href="https://fonts.googleapis.com/css2?family=Open+Sans:ital,wght@0,400;0,600;0,700;1,400&display=swap" rel="stylesheet">
<style>
:root{
  --orange:#e2672d;
  --band:#3b4048;
  --blue:#2c6da6;
  --hero-dark:#0a2348;
  --hero-mid:#1d5a9a;
  --hero-light:#6fb4e6;
  --glow:#e0523a;
  --text:#666a70;
  --muted:#9a9ea4;
  --line:#e3e5e8;
  --bg:#ffffff;
}
*{box-sizing:border-box;margin:0;padding:0}
html,body{width:813px;height:1200px;overflow:hidden;background:var(--bg)}
body{font-family:"Open Sans",Arial,sans-serif;color:var(--text);font-size:8px;line-height:1.5;position:relative}
.wrap{position:absolute;left:62px;width:689px}

.brand{position:absolute;top:14px;left:0;width:813px;text-align:center}
.brand-dot{display:block;width:14px;height:14px;border-radius:50%;background:var(--orange);margin:0 auto 6px}
.brand-name{font-size:26px;font-weight:400;color:var(--blue);line-height:1.2}

.band{top:100px;height:27px;background:var(--band)}
.band-accent{position:absolute;left:0;top:0;width:54px;height:27px;background:var(--orange)}

.hero{top:127px;height:410px;overflow:hidden;
  background:
    radial-gradient(ellipse 150px 90px at 36% 52%,rgba(224,82,58,.55),rgba(224,82,58,0) 70%),
    radial-gradient(ellipse 260px 170px at 40% 48%,rgba(160,215,250,.55),rgba(160,215,250,0) 70%),
    linear-gradient(120deg,var(--hero-dark) 0%,var(--hero-mid) 45%,var(--hero-light) 75%,#2a6db0 100%)}
.dots{position:absolute;left:14px;bottom:14px;display:flex;gap:4px}
.dots span{width:5px;height:5px;border-radius:50%;background:rgba(255,255,255,.5)}
.dots span:first-child{background:#fff}

.form{position:absolute;right:19px;top:57px;width:190px;background:#fff;padding:16px 14px;box-shadow:0 2px 6px rgba(0,0,0,.25)}
.form h2{color:var(--orange);font-size:14px;font-weight:600;margin-bottom:12px;line-height:1.2}
.field{height:22px;border:1px solid #d6d8db;margin-bottom:8px;font-size:7px;color:var(--muted);padding:0 6px;display:flex;justify-content:space-between;align-items:center}
.btn{display:block;background:var(--orange);color:#fff;font-size:8px;font-weight:700;text-align:center;height:24px;line-height:24px;margin-top:12px}

h3.section{color:var(--blue);font-size:10.5px;font-weight:700;text-transform:uppercase;line-height:1.3}

.about{top:563px;width:470px}
.about-body{display:flex;gap:14px;margin-top:14px}
.doctor{width:100px;height:92px;flex:none;background:linear-gradient(180deg,#dfe6ee,#b9c6d4)}
.about p{font-size:7px;line-height:1.75}

.testimonials{top:563px;left:564px;width:187px}
.quote{margin-top:14px;padding-left:16px;position:relative;color:var(--blue);font-style:italic;font-size:7px;line-height:1.75}
.quote:before{content:"\201C";position:absolute;left:0;top:-6px;font-size:22px;color:var(--orange);font-style:normal}
.author{margin-top:8px;padding-left:16px;font-size:6.5px;color:var(--text);font-style:italic}

.conditions{top:707px}
.conditions .head{display:flex;align-items:center;gap:10px}
.conditions .head:after{content:"";flex:1;height:1px;background:var(--line)}
.cards{display:flex;gap:9px;margin-top:18px}
.card{width:165px}
.card-img{height:108px}
.img-1{background:linear-gradient(160deg,#d9cbbd,#a88c72)}
.img-2{background:linear-gradient(160deg,#e6d8cc,#b79a82)}
.img-3{background:linear-gradient(160deg,#c6b3a4,#7d6454)}
.img-4{background:linear-gradient(160deg,#dfd2dc,#a98ea5)}
.card h4{font-size:8px;font-weight:600;color:#44484e;margin-top:10px}
.card p{font-size:6.5px;line-height:1.6;margin-top:4px;height:32px}
.more{display:inline-block;background:var(--orange);color:#fff;font-size:6px;font-weight:700;padding:4px 9px;margin-top:8px}

.news{top:1010px}
.news-item{display:flex;gap:14px;margin-top:16px;padding-bottom:22px;border-bottom:1px solid var(--line)}
.date{width:50px;flex:none;color:var(--blue);font-weight:700;font-size:11px;line-height:1.3}
.news-item h5{color:var(--blue);font-size:8.5px;font-weight:700}
.news-item p{font-size:7px;margin-top:4px;line-height:1.7}

.footer{top:1148px;display:flex;justify-content:space-between;align-items:flex-start}
.footer-links{font-size:7px;color:var(--text)}
.footer-links span{margin:0 4px;color:var(--muted)}
.copy{font-size:6.5px;color:var(--muted);margin-top:6px}
.social{display:flex;gap:6px}
.social span{width:18px;height:18px;border-radius:50%;background:var(--blue)}
</style>
</head>
<body>

<header class="brand">
  <span class="brand-dot"></span>
  <div class="brand-name">Carpal Tunnel Syndrome</div>
</header>

<div class="wrap band"><span class="band-accent"></span></div>

<section class="wrap hero" role="img" aria-label="Glowing blue X-ray of a hand and wrist with the carpal bones highlighted in red">
  <div class="dots"><span></span><span></span><span></span><span></span><span></span></div>
  <form class="form" aria-label="Get a free diagnosis">
    <h2>GET A FREE DIAGNOSIS</h2>
    <div class="field">Name</div>
    <div class="field">Phone</div>
    <div class="field">Email</div>
    <div class="field">Requested Appointment Time
      <svg width="6" height="4" viewBox="0 0 6 4"><path d="M0 0h6L3 4z" fill="#9a9ea4"/></svg>
    </div>
    <span class="btn">GET APPOINTMENT</span>
  </form>
</section>

<section class="wrap about">
  <h3 class="section">What is Carpal Tunnel Syndrome</h3>
  <div class="about-body">
    <div class="doctor" role="img" aria-label="Portrait photo of the doctor in a white coat"></div>
    <p>In its earliest stages, carpal tunnel syndrome causes numbness and tingling in the thumb, index and middle fingers. Pressure on the median nerve inside the wrist builds slowly, often worse at night. Early diagnosis keeps treatment simple and protects grip strength for the long term. Splints, therapy and minor surgery can all help.</p>
  </div>
</section>

<aside class="wrap testimonials">
  <h3 class="section">Testimonials</h3>
  <p class="quote">After months of numb fingers I could finally sleep through the night. The care was calm, clear and quick, and my hands feel strong again.</p>
  <p class="author">Rosa Lind, City Name</p>
</aside>

<section class="wrap conditions">
  <div class="head"><h3 class="section">Other conditions treated by Dr. Halvorsen:</h3></div>
  <div class="cards">
    <article class="card">
      <div class="card-img img-1" role="img" aria-label="Photo of a person holding a sore elbow"></div>
      <h4>Cubital Tunnel Syndrome</h4>
      <p>Pressure on the ulnar nerve at the elbow causes tingling in the ring and little fingers.</p>
      <span class="more">READ MORE</span>
    </article>
    <article class="card">
      <div class="card-img img-2" role="img" aria-label="Photo of a hand with a painful thumb tendon"></div>
      <h4>De Quervain's Tenosynovitis</h4>
      <p>Painful swelling of tendons at the base of the thumb, often linked to repeated gripping.</p>
      <span class="more">READ MORE</span>
    </article>
    <article class="card">
      <div class="card-img img-3" role="img" aria-label="Photo of a palm with bent fingers"></div>
      <h4>Dupuytren's Disease</h4>
      <p>A slow thickening of tissue in the palm that pulls fingers into a bent position.</p>
      <span class="more">READ MORE</span>
    </article>
    <article class="card">
      <div class="card-img img-4" role="img" aria-label="Photo of an injured hand being examined"></div>
      <h4>Hand Fractures</h4>
      <p>Breaks in the small bones of the hand treated with splints, pins or careful surgery.</p>
      <span class="more">READ MORE</span>
    </article>
  </div>
</section>

<section class="wrap news">
  <h3 class="section">News</h3>
  <div class="news-item">
    <div class="date">AUG<br>11/15</div>
    <div>
      <h5>New wrist clinic hours start this month with early morning and evening visits available</h5>
      <p>Patients can now book a free diagnosis before or after work. Call our front desk or use the form above to choose a time that suits you.</p>
    </div>
  </div>
</section>

<footer class="wrap footer">
  <div>
    <div class="footer-links">About us<span>|</span>Our services<span>|</span>Digital Scan<span>|</span>Our Products<span>|</span>Partners</div>
    <div class="copy">Copyright 2015 All Rights Reserved. Carpal Tunnel Syndrome</div>
  </div>
  <div class="social" aria-label="Social links"><span></span><span></span><span></span><span></span></div>
</footer>

</body>
</html>
```